Lirra Dusk a young drag queen needs a website to promote herself

URLs: queenlirra.example / lirradusk.example
General Requests
• SEO-Optimized
• CMS: Joomla
Lirra Dusk is a young Drag queen still going to college and living in the us. She has an international Background with Canadian and Swiss citizenship. She is very creative not only in her Shows but she is also a painter, a Fashion designer a Music writer, a singer and an excellent vegan cook.

In order to promote her and to book her for a Show or a maquillage she needs a Website that will highly interact with social Media.

The Structure of the Website could be as follows:

Welcome page
From the Welcome page navigation to
1. Blog
a. Easy tool to add new Blogs
b. Possibility for others to write comments
c. Possibilty to
2. Events: Videos and Pictures
a. Easy Way to Ad Pictures and Vidoes and Showing a Title/Description
3. Upcoming Events and Shows
a. Possibility to describe Upcoming shows with link for more Information and Registration
4. Book a Show
a. I offer a lot of different Shows with Dancing, Singing or Moderating an Evening. Since I Speak English, (Swiss-)German and French I can entertain a multicultural Audience. Just get in touch with me and let’s discuss it.
b. Contact form for ordering an offer for a show (Name and Address; Kind of Show, Duration, Date, Place, Budget, Captcha)
c. lirra@lirradusk.example
5. Book a Maquillage
a. Do you want to look like a Drag? Are you a young Drag and want to learn how to get dressed up an a unique Maquillage? Do you want to have a special surprise for a Bachelors Party? Just ask me! I’m your Expert! Also available as Gift Certificate.
b. Contact form for ordering an offer for a Maquillage (Name and Address; Kind of Maquillage, Option for Gift Certificate; Occasion, Date, Place, Budget; captcha);
c. Form mailed to lirra@lirradusk.example
6. Lirra on Social Media
a. Join me on Facebook
b. Join me on Instagram
c. Join me on Soundcloud
7. Sponsors and Partners
a. Banner Glow Mesa
b. ….
Updates

Industry/Entity Type

College

Number of Pages Required

5+ page

Font styles to use
Decorative

Colors
6b449b
d2a4cc
e4daeb

Requirements
Must have
• Responsive Design

```html
<!DOCTYPE html>
<html lang="en">
<head>
<meta charset="utf-8">
<title>Lirra Dusk</title>
<link rel="stylesheet" href="https://fonts.googleapis.com/css2?family=Arimo:wght@400;700&family=Oswald:wght@300;400&display=swap">
<style>
:root{
  --ink:#1d1d1d;
  --header:#1f1f1f;
  --nav-top:#5a475a;
  --nav-bottom:#3e323f;
  --gold:#f2b84a;
  --gold-dark:#d99a2b;
  --white:#ffffff;
  --text:#444444;
  --panel:rgba(20,18,16,.78);
  --field:#ffffff;
  --field-text:#7a7a7a;
  --band:#f2f2f2;
  --footer:#262626;
  --purple:#6b449b;
  --lilac:#d2a4cc;
  --mist:#e4daeb;
}
*{margin:0;padding:0;box-sizing:border-box}
html,body{width:1200px;height:2228px;overflow:hidden}
body{position:relative;font-family:"Arimo",Arial,sans-serif;color:var(--ink);background:var(--white)}
.abs{position:absolute}

.site-header{left:0;top:0;width:1200px;height:92px;background:var(--header)}
.site-title{left:74px;top:30px;font-size:32px;font-weight:700;color:var(--white);letter-spacing:.3px}

.main-nav{left:0;top:92px;width:1200px;height:51px;background:linear-gradient(var(--nav-top),var(--nav-bottom));display:flex;align-items:center;padding-left:78px;gap:0}
.main-nav a{color:var(--white);font-size:13px;text-decoration:none;margin-right:53px;white-space:nowrap}

.hero{left:0;top:143px;width:1200px;height:571px;background:linear-gradient(160deg,#b5946c 0%,#8a6c4b 30%,#a08262 55%,#6b5339 80%,#4e3c2b 100%)}
.hero-figure{left:505px;top:20px;width:150px;height:540px;border-radius:60px 60px 20px 20px;background:linear-gradient(#c9a25a,#8a6a2e 60%,#5d4522);opacity:.55}

.booking{left:74px;top:481px;width:1052px;height:192px;background:var(--panel)}
.booking h2{position:absolute;left:0;top:29px;width:100%;text-align:center;color:var(--white);font-size:27px;font-weight:700}
.field{height:33px;background:var(--field);color:var(--field-text);font-size:12px;line-height:33px;padding-left:14px}
.field.select::after,.field.date::after{content:"";position:absolute;right:14px;top:12px;width:6px;height:6px;border-right:1.5px solid #555;border-bottom:1.5px solid #555;transform:rotate(45deg)}
.field.date::after{border:1.5px solid #555;transform:none;width:9px;height:9px;top:11px}
.captcha-code{left:542px;top:131px;font-family:Georgia,serif;font-size:26px;font-weight:700;color:var(--white);letter-spacing:1px}
.submit{left:793px;top:126px;width:153px;height:42px;background:linear-gradient(var(--gold),var(--gold-dark));color:#3a2a10;font-size:13px;line-height:42px;text-align:center}

.section-title{left:0;width:1200px;text-align:center;font-size:27px;color:var(--ink)}
.rule{width:82px;height:3px;background:var(--gold);left:559px}

.welcome-photo{left:74px;top:824px;width:198px;height:198px;border-radius:50%;background:radial-gradient(circle at 50% 45%,#d4d0d2 0%,#9a9498 45%,#2a2628 100%)}
.welcome-text{left:307px;top:858px;width:819px;font-size:11px;line-height:22.5px;color:var(--text)}
.read-more{left:304px;top:970px;width:153px;height:46px;background:linear-gradient(var(--gold),var(--gold-dark));color:#3a2a10;font-size:13px;line-height:46px;text-align:center}

.events{left:0;top:1066px;width:1200px;height:416px;background:linear-gradient(165deg,#a87a78 0%,#c48a6a 25%,#b9735e 45%,#5a3f5f 70%,#1d2450 100%)}
.events .section-title{top:38px;font-size:31px}
.event{top:110px;width:222px;text-align:center;color:var(--white)}
.event-date{font-family:"Oswald",sans-serif;font-weight:400;font-size:80px;line-height:92px}
.event-date small{font-size:34px;font-weight:300}
.event p{margin-top:12px;font-size:11px;line-height:22.5px;text-align:justify;text-align-last:center}
.event .dash{width:33px;height:3px;background:var(--white);margin:22px auto 0}

.videos .section-title{top:1534px;font-size:31px}
.thumb{top:1620px;width:331px;height:208px}
.thumb svg{position:absolute;left:139px;top:78px}

.sponsors{left:0;top:1901px;width:1200px;height:243px;background:var(--band)}
.sponsors .section-title{top:42px;font-size:29px}
.partner{top:105px;width:142px;height:83px;background:var(--white);display:flex;align-items:center;justify-content:center;gap:6px;font-size:13px;font-weight:700;color:var(--purple)}
.partner i{display:block;width:14px;height:14px;background:var(--lilac)}
.partner i.round{border-radius:50%}

.site-footer{left:0;top:2144px;width:1200px;height:84px;background:var(--footer)}
.copyright{left:74px;top:32px;font-size:11px;color:#dddddd}
.social{top:26px;width:32px;height:32px;border-radius:50%;background:var(--purple)}
</style>
</head>
<body>

<header class="site-header abs">
  <div class="site-title abs">Lirra Dusk</div>
</header>

<nav class="main-nav abs">
  <a href="#">Home</a>
  <a href="#">Blog</a>
  <a href="#">Events</a>
  <a href="#">Book a Show</a>
  <a href="#">Book a Maquillage</a>
  <a href="#">Lirra on Social Media</a>
  <a href="#">Sponsors &amp; Partners</a>
  <a href="#">Contact us</a>
</nav>

<section class="hero abs" role="img" aria-label="Lirra Dusk in a gold sequined gown and crown standing before sandstone rocks">
  <div class="hero-figure abs"></div>
</section>

<form class="booking abs">
  <h2>Book a Show</h2>
  <div class="field abs" style="left:24px;top:80px;width:238px">Name &amp; Address</div>
  <div class="field abs" style="left:279px;top:80px;width:238px">Kind of Show</div>
  <div class="field select abs" style="left:536px;top:80px;width:238px">---Duration----</div>
  <div class="field date abs" style="left:793px;top:80px;width:238px">Date: dd/mm/yyyy</div>
  <div class="field select abs" style="left:24px;top:126px;width:238px">---Select Place---</div>
  <div class="field select abs" style="left:279px;top:126px;width:238px">---Select Budget---</div>
  <div class="captcha-code abs">78gh21</div>
  <div class="field abs" style="left:645px;top:126px;width:129px">Captcha</div>
  <div class="submit abs">SUBMIT HERE</div>
</form>

<section class="welcome">
  <h2 class="section-title abs" style="top:770px">Welcome to Our Site Mainpage</h2>
  <div class="rule abs" style="top:813px"></div>
  <div class="welcome-photo abs" role="img" aria-label="Portrait of Lirra Dusk in dramatic gothic makeup and a black hat"></div>
  <p class="welcome-text abs">Praesent vestibulum aenean nouummy endrerit mauris. Cum sociis natoque penatibus et magnis dis parturient montes ascetur ridiculus mus. Null dui. Fusce feugiat malesuada odio. Morbi nunc odio gravida at cursus nec luctus a lorem. Praesent vestibulum aenean noummy endrerit mauris. Cum sociis natoque penatibus et magnis dis parturient montes ascetur ridiculus mus. Null dui. Fusce feugiat malesuada odio. Morbi nunc odio gravida at cursus nec luctus a lorem. Praesent vestibulum aenean noummy endrerit mauris.</p>
  <div class="read-more abs">READ MORE</div>
</section>

<section class="events abs">
  <h2 class="section-title abs">UpComming Events</h2>
  <div class="event abs" style="left:84px">
    <div class="event-date"><small>11/</small>25</div>
    <p>Praesent vestibulum aenean nonummy hendrerit mauris. Cum sociis natoque penatibus et magnis dis parturient montes ascetur ridiculus mus. Nulla dui.</p>
    <div class="dash"></div>
  </div>
  <div class="event abs" style="left:355px">
    <div class="event-date"><small>11/</small>20</div>
    <p>Praesent vestibulum aenean nonummy hendrerit mauris. Cum sociis natoque penatibus et magnis dis parturient montes ascetur ridiculus mus. Nulla dui.</p>
    <div class="dash"></div>
  </div>
  <div class="event abs" style="left:627px">
    <div class="event-date"><small>11/</small>15</div>
    <p>Praesent vestibulum aenean nonummy hendrerit mauris. Cum sociis natoque penatibus et magnis dis parturient montes ascetur ridiculus mus. Nulla dui.</p>
    <div class="dash"></div>
  </div>
  <div class="event abs" style="left:899px">
    <div class="event-date"><small>11/</small>10</div>
    <p>Praesent vestibulum aenean nonummy hendrerit mauris. Cum sociis natoque penatibus et magnis dis parturient montes ascetur ridiculus mus. Nulla dui.</p>
    <div class="dash"></div>
  </div>
</section>

<section class="videos">
  <h2 class="section-title abs">Featured Video's</h2>
  <div class="rule abs" style="top:1583px"></div>
  <div class="thumb abs" style="left:74px;background:linear-gradient(135deg,#5a6670,#c9a7b8 50%,#3a3f44)" role="img" aria-label="Video still of a performer with pink hair in a white outfit">
    <svg width="54" height="54" viewBox="0 0 54 54"><circle cx="27" cy="27" r="23" fill="none" stroke="#fff" stroke-width="5"/><path d="M21 16 L37 27 L21 38 Z" fill="#fff"/></svg>
  </div>
  <div class="thumb abs" style="left:434px;background:linear-gradient(180deg,#1a1020,#4a1f3a 55%,#120a14)" role="img" aria-label="Video still of dancers on a dark stage with red curtains">
    <svg width="54" height="54" viewBox="0 0 54 54"><circle cx="27" cy="27" r="23" fill="none" stroke="#fff" stroke-width="5"/><path d="M21 16 L37 27 L21 38 Z" fill="#fff"/></svg>
  </div>
  <div class="thumb abs" style="left:796px;background:linear-gradient(135deg,#1a1a3a,#7a2a7a 45%,#2a1a5a 80%,#111)" role="img" aria-label="Video still of dancer silhouettes under purple stage lights">
    <svg width="54" height="54" viewBox="0 0 54 54"><circle cx="27" cy="27" r="23" fill="none" stroke="#fff" stroke-width="5"/><path d="M21 16 L37 27 L21 38 Z" fill="#fff"/></svg>
  </div>
</section>

<section class="sponsors abs">
  <h2 class="section-title abs">Sponsors &amp; Partners</h2>
  <div class="partner abs" style="left:79px"><i></i>Hexaform</div>
  <div class="partner abs" style="left:257px">Brightdesk</div>
  <div class="partner abs" style="left:438px"><i class="round"></i>Fernwell</div>
  <div class="partner abs" style="left:618px"><i class="round"></i>Lumora</div>
  <div class="partner abs" style="left:799px"><i class="round"></i>Orbit Studio</div>
  <div class="partner abs" style="left:979px"><i></i>Signalpoint</div>
</section>

<footer class="site-footer abs">
  <div class="copyright abs">(c)2015, Yoursite, All Right Reserved.</div>
  <a class="social abs" style="left:980px" href="#" aria-label="Social link"></a>
  <a class="social abs" style="left:1016px" href="#" aria-label="Social link"></a>
  <a class="social abs" style="left:1052px" href="#" aria-label="Social link"></a>
  <a class="social abs" style="left:1088px" href="#" aria-label="Social link"></a>
</footer>

</body>
</html>
```